Harlow Ridge Partners Business Cards

Design Business cards in a format where I can change the information and utilize a third party buisness card printing company

Contact Information for Business Card

Want Logo and Name on Back. Looking for Spot UV style shine on Logo. Probably Black background. Want smaller logo on front with contact details. Like rounded edges or something else interesting.

Requirements
Must have
• Strong masculine look.

```html
<!DOCTYPE html>
<html lang="en">
<head>
<meta charset="utf-8">
<title>Harlow Ridge Partners – Business Cards</title>
<link href="https://fonts.googleapis.com/css2?family=Arimo:wght@400;700&display=swap" rel="stylesheet">
<style>
  :root {
    --canvas: #e7e4df;
    --card: #141414;
    --card-edge: #1c1c1c;
    --band: #7a7a7c;
    --band-light: #a9a9ab;
    --silver: #8e8e90;
    --silver-bright: #b4b4b6;
    --text: #c9c9cb;
  }
  * { margin: 0; padding: 0; box-sizing: border-box; }
  html, body { width: 1200px; height: 886px; overflow: hidden; }
  body {
    background: var(--canvas);
    font-family: "Arimo", Arial, sans-serif;
    position: relative;
  }
  .card {
    position: absolute;
    top: 148px;
    width: 336px;
    height: 590px;
    background: var(--card);
    box-shadow: 0 10px 30px rgba(0,0,0,0.25);
    overflow: hidden;
  }
  .card--front { left: 196px; border-radius: 8px; }
  .card--back { left: 668px; border-radius: 26px; }

  .edge-band {
    position: absolute;
    left: 0; right: 0;
    height: 14px;
    background: linear-gradient(var(--band-light), var(--band));
  }
  .edge-band::after {
    content: "";
    position: absolute;
    left: 0; right: 0;
    height: 3px;
    background: var(--card-edge);
  }
  .edge-band--top { top: 0; }
  .edge-band--top::after { bottom: 4px; }
  .edge-band--bottom { bottom: 0; }
  .edge-band--bottom::after { top: 4px; }

  .brand {
    position: absolute;
    left: 0; right: 0;
    display: flex;
    flex-direction: column;
    align-items: center;
    gap: 14px;
    text-align: center;
  }
  .brand__mark {
    width: 16px; height: 16px;
    background: var(--silver);
  }
  .brand__name {
    color: var(--silver);
    font-weight: 700;
    text-transform: uppercase;
    letter-spacing: 0.08em;
    line-height: 1.25;
  }
  .card--front .brand { top: 92px; }
  .card--front .brand__name { font-size: 22px; }
  .card--back .brand { top: 210px; }
  .card--back .brand__name { font-size: 32px; color: var(--silver-bright); }

  .divider {
    position: absolute;
    top: 292px;
    left: 72px; right: 72px;
    height: 2px;
    background: var(--silver);
  }
  .contact {
    position: absolute;
    top: 312px;
    left: 0; right: 0;
    text-align: center;
    color: var(--text);
    font-size: 13px;
    line-height: 1.45;
  }
  .contact__name {
    font-size: 17px;
    font-weight: 700;
    color: var(--silver);
    letter-spacing: 0.04em;
  }
  .contact__title {
    font-size: 13px;
    font-weight: 700;
    margin-bottom: 8px;
  }
  .contact__label { font-weight: 700; }
</style>
</head>
<body>
  <article class="card card--front">
    <div class="edge-band edge-band--top"></div>

    <div class="brand">
      <span class="brand__mark"></span>
      <span class="brand__name">Harlow Ridge<br>Partners</span>
    </div>

    <div class="divider"></div>

    <div class="contact">
      <p class="contact__name">MARCUS HALE</p>
      <p class="contact__title">CEO/FOUNDER</p>
      <p>4120 Cedar Hollow Road Juneau,<br>Alaska 99801</p>
      <p><span class="contact__label">P:</span> 907 555 0142 <span class="contact__label">M:</span> 907 555 0187</p>
      <p><span class="contact__label">F:</span> 907 555 0163 <span class="contact__label">E:</span> marcus@harlowridge.com</p>
      <p><span class="contact__label">W:</span> www.harlowridge.com</p>
    </div>

    <div class="edge-band edge-band--bottom"></div>
  </article>

  <article class="card card--back">
    <div class="brand">
      <span class="brand__mark"></span>
      <span class="brand__name">Harlow Ridge<br>Partners</span>
    </div>
  </article>
</body>
</html>
```